New Helpnest Support needs a website design

We need a web design for a new product we are developing that provides tech support to consumers for a small ongoing monthly fee. We are looking for a fresh, technology look and feel. We want the site to have a tech feel - yet not intimidating. Simple and welcoming. We are in need of an initial landing page, sign on page, and a product home page.

Thank you to everyone who submitted designs. It was a very difficult decision!

Tech

```html
<!DOCTYPE html>
<html lang="en">
<head>
<meta charset="utf-8">
<title>Helpnest Support</title>
<link rel="stylesheet" href="https://fonts.googleapis.com/css2?family=Roboto+Condensed:wght@300;400;700&family=Open+Sans:wght@400;600;700&display=swap">
<style>
:root{
  --green:#8fc43e;
  --green-dark:#6f9e2a;
  --navy:#2d3949;
  --navy-deep:#253041;
  --navy-line:#3d4a5c;
  --white:#ffffff;
  --text-soft:#c9d0da;
  --ink:#2a2f36;
}
*{margin:0;padding:0;box-sizing:border-box}
html,body{width:1200px;height:2840px;overflow:hidden}
body{background:var(--navy);font-family:"Open Sans",Arial,sans-serif;color:var(--white);position:relative}
.abs{position:absolute}
.topbar{left:0;top:0;width:1200px;height:18px;background:var(--navy-deep)}
.topbar .signin{position:absolute;right:180px;top:2px;font-size:11px;color:var(--green);letter-spacing:1px}
.header{left:0;top:18px;width:1200px;height:88px;background:var(--white);border-bottom:2px solid #e6e6e6}
.brand{position:absolute;left:188px;top:24px;font-family:"Roboto Condensed",Arial,sans-serif;font-size:34px;font-weight:400;color:var(--navy)}
.nav{position:absolute;left:550px;top:36px;display:flex}
.nav a{font-size:13px;color:var(--ink);text-decoration:none;padding:0 25px;border-left:1px solid #ddd;font-weight:600}
.nav a:first-child{border-left:none}
.hero{left:0;top:106px;width:1200px;height:444px;background:linear-gradient(180deg,#98cc48,#86ba36)}
.hero .person{position:absolute;left:265px;top:88px;width:250px;height:356px;border-radius:120px 120px 0 0;background:linear-gradient(180deg,#b89a7e 0%,#8a7766 28%,#4d5561 45%,#3b4350 100%)}
.bubble{position:absolute;left:540px;top:135px;width:418px;height:80px;background:var(--navy);padding:14px 20px;font-family:"Roboto Condensed",Arial,sans-serif;font-weight:700;font-size:22px;line-height:26px;color:var(--white)}
.bubble-tail{position:absolute;left:548px;top:214px}
.btn{position:absolute;background:var(--navy);color:var(--green);font-family:"Roboto Condensed",Arial,sans-serif;font-weight:700;text-align:center}
.hero .btn{left:656px;top:310px;width:132px;height:42px;line-height:42px;font-size:20px}
.arrow{position:absolute;top:205px;font-size:40px;color:var(--white);font-family:"Open Sans",sans-serif}
.title{left:0;width:1200px;text-align:center;font-family:"Roboto Condensed",Arial,sans-serif;font-weight:300;color:var(--green);font-size:38px}
.title.upper{text-transform:uppercase}
.lead{left:188px;width:824px;font-size:13px;line-height:18px;color:var(--text-soft)}
.features{left:188px;top:780px;width:824px;height:390px}
.features .vline{position:absolute;left:412px;top:0;width:1px;height:390px;background:var(--navy-line)}
.features .hline{position:absolute;left:0;top:192px;width:824px;height:1px;background:var(--navy-line)}
.feature{position:absolute;width:300px}
.feature svg{position:absolute;left:0;top:0}
.feature h3{position:absolute;left:60px;top:28px;font-family:"Roboto Condensed",Arial,sans-serif;font-weight:700;font-size:22px;white-space:nowrap}
.feature p{position:absolute;left:60px;top:62px;width:220px;font-size:12px;line-height:16px;color:var(--text-soft)}
.gallery{left:188px;top:1446px;width:824px;height:394px;display:grid;grid-template-columns:repeat(3,1fr);grid-template-rows:repeat(2,1fr);gap:4px}
.gallery div{width:100%;height:100%}
.caption{left:0;width:1200px;text-align:center;font-size:13px;color:var(--text-soft)}
.rule{left:188px;width:824px;height:1px;background:var(--navy-line)}
.devices{left:195px;top:2077px;width:390px;height:240px;background:linear-gradient(135deg,#4a7aa8 0%,#2c4d72 60%,#1a2533 100%)}
.work{left:612px;top:2090px;width:400px;height:240px}
.work h3{font-family:"Roboto Condensed",Arial,sans-serif;font-weight:700;font-size:32px}
.work p{margin-top:10px;font-size:12px;line-height:16px;color:var(--text-soft)}
.work .btn-green{position:absolute;left:10px;top:190px;background:var(--green);color:var(--navy);font-size:12px;font-weight:700;padding:5px 12px}
.avatar{left:555px;top:2458px;width:90px;height:90px;border-radius:50%;background:linear-gradient(180deg,#d9c3ad,#7a8594);border:4px solid var(--white)}
.quote{left:270px;top:2560px;width:660px;font-size:13px;line-height:19px;color:var(--text-soft);text-align:center}
.qmark{font-family:Georgia,serif;font-size:70px;color:var(--green);line-height:1}
.author{left:0;top:2630px;width:1200px;text-align:center;font-size:12px;color:var(--green)}
.band{left:0;top:2698px;width:1200px;height:18px;background:var(--green)}
.footer{left:0;top:2716px;width:1200px;height:124px;background:var(--navy-deep)}
.fnav{position:absolute;left:188px;top:26px;display:flex}
.fnav a{font-size:13px;color:var(--white);text-decoration:none;margin-right:40px}
.social{position:absolute;left:904px;top:18px;display:flex;gap:8px}
.social span{width:30px;height:30px;border:2px solid var(--white);border-radius:50%}
.copy{position:absolute;left:0;top:86px;width:1200px;text-align:center;font-size:11px;color:var(--text-soft)}
</style>
</head>
<body>
<div class="abs topbar"><span class="signin">SIGN IN</span></div>

<header class="abs header">
  <div class="brand">Helpnest Support</div>
  <nav class="nav"><a>Home</a><a>About Us</a><a>Service</a><a>Our Work</a><a>Product</a><a>Reach Us</a></nav>
</header>

<section class="abs hero">
  <span class="arrow" style="left:175px">‹</span>
  <span class="arrow" style="left:1000px">›</span>
  <div class="person" role="img" aria-label="Photo of a smiling support agent in a grey suit"></div>
  <div class="bubble">LOREM IPSUM DOLOR SIT AMET,<br>CONSECTETUER ADIPISCING ELIT</div>
  <svg class="bubble-tail" width="24" height="16"><polygon points="0,0 24,0 0,16" fill="#2d3949"/></svg>
  <div class="btn">Read More</div>
</section>

<h2 class="abs title upper" style="top:578px">About Us</h2>
<p class="abs lead" style="top:656px">Sed ut perspiciatis unde omnis iste natus error sit voluptatem accusantium doloremque laudantium, totam rem aperiam, eaque ipsa quae ab illo inventore veritatis et quasi architecto beatae vitae dicta sunt explicabo. Nemo enim ipsam voluptatem quia voluptas sit aspernatur aut odit aut fugit, sed quia consequuntur magni dolores eos qui ratione voluptatem sequi nesciunt. Neque porro quisquam est, qui dolorem ipsum quia dolor sit amet, consectetur adipisci velit, sed quia non numquam eius modi tempora incidunt ut labore et dolore magnam aliquam quaerat.</p>

<section class="abs features">
  <div class="vline"></div><div class="hline"></div>
  <div class="feature" style="left:0;top:50px">
    <svg width="44" height="50" viewBox="0 0 44 50"><rect x="6" y="2" width="32" height="46" rx="4" fill="none" stroke="#8fc43e" stroke-width="3"/><circle cx="22" cy="41" r="2.5" fill="#8fc43e"/></svg>
    <h3>LOREM IPSUM DOLOR</h3>
    <p>Lorem ipsum dolor sit amet, consectetur adipiscing elit, sed do eiusmod tempor incididunt.</p>
  </div>
  <div class="feature" style="left:454px;top:50px">
    <svg width="48" height="48" viewBox="0 0 48 48" fill="none" stroke="#8fc43e" stroke-width="3"><circle cx="24" cy="24" r="20"/><ellipse cx="24" cy="24" rx="9" ry="20"/><line x1="4" y1="24" x2="44" y2="24"/><line x1="8" y1="13" x2="40" y2="13"/><line x1="8" y1="35" x2="40" y2="35"/></svg>
    <h3>LOREM IPSUM DOLOR</h3>
    <p>Lorem ipsum dolor sit amet, consectetur adipiscing elit, sed do eiusmod tempor incididunt.</p>
  </div>
  <div class="feature" style="left:0;top:240px">
    <svg width="48" height="48" viewBox="0 0 48 48"><g fill="#8fc43e"><circle cx="18" cy="22" r="12"/><rect x="15" y="4" width="6" height="36"/><rect x="0" y="19" width="36" height="6"/><rect x="15" y="4" width="6" height="36" transform="rotate(45 18 22)"/><rect x="15" y="4" width="6" height="36" transform="rotate(-45 18 22)"/><circle cx="38" cy="38" r="7"/></g><circle cx="18" cy="22" r="5" fill="#2d3949"/><circle cx="38" cy="38" r="3" fill="#2d3949"/></svg>
    <h3>LOREM IPSUM DOLOR</h3>
    <p>Lorem ipsum dolor sit amet, consectetur adipiscing elit, sed do eiusmod tempor incididunt.</p>
  </div>
  <div class="feature" style="left:454px;top:240px">
    <svg width="48" height="48" viewBox="0 0 48 48" fill="#8fc43e"><rect x="4" y="32" width="8" height="14"/><rect x="16" y="24" width="8" height="22"/><rect x="28" y="16" width="8" height="30"/><polyline points="4,24 18,14 28,18 42,4" fill="none" stroke="#8fc43e" stroke-width="3"/><polygon points="44,2 44,12 34,2"/></svg>
    <h3>LOREM IPSUM DOLOR</h3>
    <p>Lorem ipsum dolor sit amet, consectetur adipiscing elit, sed do eiusmod tempor incididunt.</p>
  </div>
</section>

<h2 class="abs title" style="top:1270px">Service</h2>
<p class="abs caption" style="top:1336px;line-height:20px">Lorem ipsum dolor sit amet, consectetur adipiscing elit, sed do eiusmod<br>tempor incididunt.</p>
<section class="abs gallery">
  <div role="img" aria-label="Photo of a businessman on the phone" style="background:linear-gradient(135deg,#4f86b8,#2b4e78)"></div>
  <div role="img" aria-label="Photo of a laptop and pen on a desk" style="background:linear-gradient(135deg,#cfc8bd,#7b756c)"></div>
  <div role="img" aria-label="Photo of a cheering businesswoman among office towers" style="background:linear-gradient(135deg,#9fb4c9,#4b5f78)"></div>
  <div role="img" aria-label="Photo of a hand drawing a rising arrow" style="background:linear-gradient(135deg,#e7eef5,#7f97b2)"></div>
  <div role="img" aria-label="Photo of a team meeting around a chart" style="background:linear-gradient(135deg,#e4e6e9,#9aa3ad)"></div>
  <div role="img" aria-label="Photo of a hand holding a glowing globe" style="background:linear-gradient(135deg,#1d3a6e,#0c1a38)"></div>
</section>
<p class="abs caption" style="top:1874px">Lorem ipsum dolor sit amet, consectetur adipiscing elit, sed do eiusmod tempor incididunt.</p>
<div class="abs rule" style="top:1945px"></div>

<h2 class="abs title" style="top:1985px">Our Work</h2>
<div class="abs devices" role="img" aria-label="Photo of a desktop monitor and laptop showing a business website"></div>
<section class="abs work">
  <h3>LOREM IPSUM</h3>
  <p>Sed ut perspiciatis unde omnis iste natus error sit voluptatem accusantium doloremque laudantium, totam rem aperiam, eaque ipsa quae ab illo inventore veritatis et quasi architecto beatae vitae dicta sunt explicabo. Nemo enim ipsam voluptatem quia voluptas sit aspernatur aut odit aut fugit, sed quia consequuntur magni dolores eos qui ratione sequi nesciunt. Neque porro quisquam est qui dolorem ipsum quia dolor sit amet.</p>
  <span class="btn-green">Read More</span>
</section>
<div class="abs rule" style="top:2360px"></div>

<h2 class="abs title" style="top:2393px">Testimonial</h2>
<div class="abs avatar" role="img" aria-label="Portrait of a satisfied customer"></div>
<span class="abs qmark" style="left:228px;top:2548px">“</span>
<p class="abs quote">Lorem ipsum dolor sit amet, consectetur adipiscing elit, sed do eiusmod tempor incididunt ut labore et dolore magna aliqua. Ut enim ad minim veniam, quis nostrud exercitation ullamco laboris nisi ut aliquip ex ea commodo consequat.</p>
<span class="abs qmark" style="left:940px;top:2590px">”</span>
<p class="abs author">Marco</p>

<div class="abs band"></div>
<footer class="abs footer">
  <nav class="fnav"><a>Home</a><a>About Us</a><a>Service</a><a>Our Work</a><a>Product</a><a>Reach Us</a></nav>
  <div class="social"><span></span><span></span><span></span></div>
  <p class="copy">Copyright Privacy 2014</p>
</footer>
</body>
</html>
```